web site update

I want to get a better website for a small high end remodeling and construction company
I currently have a web site but you will find that it is not good.
www.pelbrookhaven.com
We are a high end construction / remodeling company that has been in business since 2003. We primarily work in the mid peninsula of the bay area. Most of our clientele are very educated captains of industry. This group is still the target client.
I had my logo designed by Vellum Forge a few years ago and I do like it, I like the orange and black or orange a blue. I don’t have a lot of content on hand as far as professional photographs.
Number of pages not sure and are open to: design pages vs full function website
I think what I am after is a web presence that will seal the deal as we are getting high referrals from past clients.
Construction
1 page

```html
<!DOCTYPE html>
<html lang="en">
<head>
<meta charset="utf-8">
<title>Pelbrook Haven Remodeling</title>
<link href="https://fonts.googleapis.com/css2?family=Raleway:wght@400;500;600;700&display=swap" rel="stylesheet">
<style>
  :root {
    --orange: #ff6a00;
    --ink: #1b1b1b;
    --text: #444444;
    --muted: #777777;
    --rule: #9a9a9a;
    --panel: #f5f5f5;
    --panel-grey: #eeeff1;
    --navy: #253252;
    --black: #000000;
    --white: #ffffff;
  }
  * { box-sizing: border-box; margin: 0; padding: 0; }
  html, body { width: 1200px; height: 3614px; overflow: hidden; }
  body { font-family: "Raleway", sans-serif; color: var(--text); background: var(--white); position: relative; }
  section, header, footer { position: relative; width: 1200px; }

  /* Header */
  .site-header { height: 200px; }
  .brand { position: absolute; left: 58px; top: 68px; display: flex; align-items: center; gap: 18px; }
  .brand-mark { width: 70px; height: 70px; background: var(--ink); }
  .brand-name { font-weight: 700; font-size: 24px; line-height: 1.15; color: var(--orange); letter-spacing: 1px; }
  .contact { position: absolute; left: 890px; top: 26px; font-size: 20px; color: var(--ink); }
  .contact-row { display: flex; align-items: center; gap: 14px; height: 36px; }
  .contact-row.phone { font-weight: 600; font-size: 23px; }
  .contact-row.address { font-size: 17px; }
  .nav { position: absolute; left: 446px; top: 100px; width: 704px; height: 60px;
         border-top: 1px solid var(--rule); border-bottom: 1px solid var(--rule);
         display: flex; align-items: center; justify-content: space-between; padding: 0 0 0 30px; font-size: 15px; color: var(--ink); }
  .nav a { color: inherit; text-decoration: none; display: flex; align-items: center; gap: 10px; }

  /* Hero */
  .hero { height: 648px; background: linear-gradient(100deg, #2c2a28 0%, #eceae6 22%, #f4f2ee 45%, #d8d4cf 62%, #3a3836 80%, #e9e7e3 100%); }
  .hero-accent { position: absolute; left: 560px; top: 150px; width: 260px; height: 80px; background: #f26a1c; opacity: .85; }

  /* Section titles */
  .section-title { position: absolute; left: 0; width: 1200px; text-align: center; font-size: 38px; font-weight: 600; color: var(--ink); }
  .section-title .accent { color: var(--orange); }
  .section-title::after { content: ""; display: block; width: 240px; height: 2px; background: var(--ink); margin: 12px auto 0; }

  /* About */
  .about { height: 397px; }
  .about .section-title { top: 70px; }
  .about-copy { position: absolute; left: 50px; top: 172px; width: 826px; font-size: 13.5px; line-height: 1.45; text-align: justify; color: var(--text); }
  .about-copy p + p { margin-top: 18px; }
  .about-badge { position: absolute; left: 930px; top: 220px; display: flex; align-items: center; gap: 14px; font-weight: 600; font-size: 18px; color: var(--ink); }
  .about-badge .square { width: 46px; height: 46px; background: var(--ink); }

  /* Services */
  .services { height: 675px; background: var(--panel); }
  .services .section-title { top: 78px; }
  .service { position: absolute; top: 217px; width: 333px; }
  .service-photo { height: 203px; }
  .service h3 { margin-top: 26px; font-size: 21px; font-weight: 700; color: var(--ink); }
  .service p { margin-top: 14px; font-size: 13.5px; line-height: 1.42; text-align: justify; }
  .btn { display: inline-block; margin-top: 20px; background: var(--orange); color: var(--white); font-weight: 600; font-size: 16px; padding: 8px 18px; }

  /* Gallery */
  .gallery { height: 825px; }
  .gallery .section-title { top: 68px; }
  .tile { position: absolute; width: 318px; height: 249px; }
  .tile-feature { background: #141414; color: var(--white); padding: 30px 18px 0; }
  .tile-feature h4 { font-size: 16px; font-weight: 600; }
  .tile-feature p { margin-top: 16px; font-size: 14px; line-height: 1.4; }
  .tile-feature .btn { position: absolute; right: 14px; bottom: 26px; font-size: 13px; padding: 7px 12px; margin: 0; }

  /* Testimonial */
  .testimonial { height: 565px; background: var(--panel-grey); }
  .testimonial .section-title { top: 48px; color: var(--orange); }
  .testimonial .section-title::after { display: none; }
  .avatar { position: absolute; left: 520px; top: 148px; width: 160px; height: 160px; border-radius: 50%; background: var(--navy); }
  .quote { position: absolute; left: 240px; top: 330px; width: 720px; text-align: center; font-size: 14.5px; line-height: 1.35; color: var(--muted); }
  .dots { position: absolute; left: 0; top: 458px; width: 1200px; display: flex; justify-content: center; gap: 22px; }
  .dots span { width: 14px; height: 14px; border-radius: 50%; background: var(--orange); }

  /* Footer */
  .site-footer { height: 304px; background: var(--black); color: var(--white); }
  .social { position: absolute; top: 80px; left: 0; width: 1200px; display: flex; justify-content: center; gap: 24px; }
  .social span { width: 26px; height: 26px; background: var(--white); border-radius: 3px; }
  .footer-nav { position: absolute; top: 138px; width: 1200px; text-align: center; font-size: 15px; font-weight: 500; letter-spacing: .5px; }
  .footer-nav span { margin: 0 10px; }
  .copyright { position: absolute; top: 199px; width: 1200px; text-align: center; font-size: 14px; }
  .copyright strong { font-weight: 700; }
</style>
</head>
<body>

<header class="site-header">
  <div class="brand">
    <div class="brand-mark"></div>
    <div class="brand-name">PELBROOK HAVEN<br>REMODELING</div>
  </div>
  <div class="contact">
    <div class="contact-row phone">
      <svg width="24" height="24" viewBox="0 0 24 24" fill="none" stroke="#ff6a00" stroke-width="2"><path d="M5 3h4l2 5-2.5 1.5a11 11 0 0 0 6 6L16 13l5 2v4a2 2 0 0 1-2 2A17 17 0 0 1 3 5a2 2 0 0 1 2-2z"/></svg>
      415.555.0142
    </div>
    <div class="contact-row address">
      <svg width="24" height="24" viewBox="0 0 24 24" fill="none" stroke="#ff6a00" stroke-width="2"><path d="M12 22s7-7 7-12a7 7 0 0 0-14 0c0 5 7 12 7 12z"/><circle cx="12" cy="10" r="2.5"/></svg>
      505- Road, abc City XYZ
    </div>
  </div>
  <nav class="nav">
    <a href="#"><svg width="24" height="22" viewBox="0 0 24 22" fill="#ff6a00"><path d="M12 1 1 11h3v10h6v-6h4v6h6V11h3z"/></svg>Home</a>
    <a href="#">Gallery</a>
    <a href="#">Services</a>
    <a href="#">Questionaire</a>
    <a href="#">About Us</a>
    <a href="#">Contact Us</a>
  </nav>
</header>

<section class="hero" role="img" aria-label="Photo of a bright modern kitchen with orange cabinets and dark dining chairs">
  <div class="hero-accent"></div>
</section>

<section class="about">
  <h2 class="section-title"><span class="accent">What</span> We Do?</h2>
  <div class="about-copy">
    <p>Lorem Ipsum is simply dummy text of the printing and typesetting industry. Lorem Ipsum has been the industry's standard dummy text ever since the 1500s, when an unknown printer took a galley of type and scrambled it to make a type specimen book. It has survived not only five centuries, but also the leap into electronic typesetting, remaining essentially unchanged.</p>
    <p>Lorem Ipsum is simply dummy text of the printing and typesetting industry. Lorem Ipsum has been the industry's standard dummy text ever since the 1500s, when an unknown printer took a galley of type and scrambled it to make a type specimen book. It has survived not only five centuries, but also the leap into electronic typesetting, remaining essentially unchanged.</p>
  </div>
  <div class="about-badge">
    <div class="square"></div>
    <div>Pelbrook Haven<br>Remodeling</div>
  </div>
</section>

<section class="services">
  <h2 class="section-title"><span class="accent">Our</span> Services</h2>
  <article class="service" style="left:55px">
    <div class="service-photo" role="img" aria-label="Photo of a remodeled bathroom with glass shower" style="background:linear-gradient(120deg,#b9a98f,#efe9df 50%,#8f7b61)"></div>
    <h3>Interior Designing</h3>
    <p>It is a long established fact that a reader will be distracted by the readable content of a page when looking at its layout. The point of using Lorem Ipsum is that it has a more-or-less normal distribution of letters, as opposed to using 'Content here, content here', making it look like readable English.</p>
    <span class="btn">Read More</span>
  </article>
  <article class="service" style="left:425px">
    <div class="service-photo" role="img" aria-label="Photo of an outdoor deck with hills and blue sky" style="background:linear-gradient(180deg,#3f86c9,#bcd7ea 45%,#9a8a72 75%,#6b5e4c)"></div>
    <h3>Exterior Designing</h3>
    <p>It is a long established fact that a reader will be distracted by the readable content of a page when looking at its layout. The point of using Lorem Ipsum is that it has a more-or-less normal distribution of letters, as opposed to using 'Content here, content here', making it look like readable English.</p>
    <span class="btn">Read More</span>
  </article>
  <article class="service" style="left:808px">
    <div class="service-photo" role="img" aria-label="Photo of an arched exhibition hall with display stands" style="background:radial-gradient(ellipse at 50% 50%,#e8d7bf,#a88a68 60%,#6e5640)"></div>
    <h3>Exibition Designing</h3>
    <p>It is a long established fact that a reader will be distracted by the readable content of a page when looking at its layout. The point of using Lorem Ipsum is that it has a more-or-less normal distribution of letters, as opposed to using 'Content here, content here', making it look like readable English.</p>
    <span class="btn">Read More</span>
  </article>
</section>

<section class="gallery">
  <h2 class="section-title"><span class="accent">Gallery</span> Images</h2>
  <div class="tile tile-feature" style="left:55px;top:178px">
    <h4>Bedroom Arrangements</h4>
    <p>It is a long established fact that a reader will be distracted by the readable content of a page when looking at its layout. The point of using Lorem Ipsum is that it has a more-or-less normal distribution of letters</p>
    <span class="btn">See Full Image</span>
  </div>
  <div class="tile" style="left:443px;top:178px;background:linear-gradient(160deg,#d9d4cc,#8a4b24 60%,#5a2f16)" role="img" aria-label="Photo of a kitchen with wooden cabinets and range"></div>
  <div class="tile" style="left:832px;top:178px;background:linear-gradient(180deg,#c9a57a,#e6d6be 55%,#2e2a27)" role="img" aria-label="Photo of a room with shoji screen windows and dark counter"></div>
  <div class="tile" style="left:55px;top:493px;background:linear-gradient(180deg,#d6b998,#f3ecdf 55%,#7a4a2a)" role="img" aria-label="Photo of a bedroom with a wooden bed"></div>
  <div class="tile" style="left:443px;top:493px;background:linear-gradient(180deg,#eef0f1,#a9adb0 55%,#2a2c2e)" role="img" aria-label="Photo of a white kitchen with bar stools"></div>
  <div class="tile" style="left:832px;top:493px;background:linear-gradient(150deg,#6b3a22,#b0845a 50%,#d6c2a2)" role="img" aria-label="Photo of a granite bathroom vanity with sink"></div>
</section>

<section class="testimonial">
  <h2 class="section-title">Testimonial</h2>
  <div class="avatar" role="img" aria-label="Client portrait"></div>
  <p class="quote">Lorem Ipsum is simply dummy text of the printing and typesetting industry. Lorem Ipsum has been the industry's standard dummy text ever since the 1500s. Lorem Ipsum is simply dummy text of the printing and typesetting industry. Lorem Ipsum has been the industry's standard</p>
  <div class="dots"><span></span><span></span><span></span></div>
</section>

<footer class="site-footer">
  <div class="social"><span></span><span></span><span></span><span></span></div>
  <div class="footer-nav">HOME<span>|</span>SERVICE<span>|</span>GALLERY<span>|</span>TESTIMONIALS<span>|</span>CONTACT US</div>
  <div class="copyright">Copyrights Reserved by <strong>pelbrookhaven</strong></div>
</footer>

</body>
</html>
```